Business Card desgin, company called Stand Fast.

I am looking for the logo colors (3) to be used on the card in whatever design you think might work. the certifications are on the back (4) on the front will be my name, Dana Whitlock, owner/instructor, phone 208.555.0193, website www.sfx-drills.example, email dw@sfx-drills.example. im flexible on fonts.

Target Market(s)

firearms owners

Industry/Entity Type

firearms training

Contact Information for Business Card

certification icons on back

```html
<!DOCTYPE html>
<html lang="en">
<head>
<meta charset="utf-8">
<title>Stand Fast — Business Card</title>
<link href="https://fonts.googleapis.com/css2?family=Montserrat:wght@400;600;700;800&family=Cormorant+Garamond:wght@500&display=swap" rel="stylesheet">
<style>
  :root {
    --navy: #0d2a47;
    --navy-deep: #0a2139;
    --navy-emboss: #163a5e;
    --steel: #5f8fb0;
    --red: #c21f30;
    --white: #ffffff;
    --ink: #1b2f4a;
    --grey-text: #3a3a3a;
    --stage: #3d3d3d;
    --badge-orange: #f07f1e;
    --badge-dark: #2b2b2b;
    --badge-light: #f2f2f2;
  }
  * { margin: 0; padding: 0; box-sizing: border-box; }
  html, body {
    width: 1200px; height: 803px; overflow: hidden;
    background: var(--stage);
    font-family: "Montserrat", Arial, sans-serif;
  }
  .canvas { position: relative; width: 1200px; height: 803px; }

  .card { position: absolute; border-radius: 18px; overflow: hidden; }

  /* Front */
  .card-front {
    left: 110px; top: 100px; width: 340px; height: 600px;
    background: var(--white);
  }
  .front-header { position: absolute; left: 0; top: 0; width: 340px; height: 330px; }
  .front-header svg { display: block; }
  .front-brand {
    position: absolute; left: 0; top: 0; width: 340px; height: 300px;
    display: flex; align-items: center; justify-content: center; gap: 14px;
    color: var(--white); font-weight: 800; font-size: 30px; letter-spacing: 1px;
  }
  .brand-dot {
    width: 26px; height: 26px; border-radius: 50%; background: var(--white);
  }
  .front-body { position: absolute; left: 40px; top: 360px; right: 30px; }
  .front-wordmark {
    color: var(--red); font-weight: 800; font-size: 34px; letter-spacing: 1px;
    text-transform: uppercase; margin-bottom: 34px;
  }
  .person-name { color: var(--ink); font-weight: 700; font-size: 27px; }
  .person-title { color: var(--grey-text); font-size: 14px; margin-top: 2px; margin-bottom: 22px; }
  .contact-list { list-style: none; }
  .contact-item {
    display: flex; align-items: center; gap: 12px;
    color: var(--grey-text); font-size: 15px; line-height: 26px;
  }
  .contact-item svg { flex: none; }

  /* Back */
  .card-back {
    left: 500px; top: 250px; width: 620px; height: 370px;
    background: var(--navy);
  }
  .back-ring {
    position: absolute; left: 40px; top: 130px; width: 110px; height: 110px;
    border: 3px solid var(--navy-deep); border-radius: 50%;
  }
  .back-wordmark {
    position: absolute; left: 185px; top: 120px;
    font-weight: 800; font-size: 54px; letter-spacing: 2px; text-transform: uppercase;
    color: var(--navy-emboss);
  }
  .back-wordmark .lit { color: var(--steel); }
  .back-url {
    position: absolute; left: 190px; top: 192px;
    font-family: "Cormorant Garamond", Georgia, serif; font-weight: 500;
    font-size: 34px; letter-spacing: 1px; color: var(--navy-emboss);
  }
  .badge-row {
    position: absolute; left: 40px; right: 40px; bottom: 34px;
    display: flex; justify-content: space-between; align-items: flex-end;
  }
  .badge { width: 74px; height: 80px; }
</style>
</head>
<body>
<main class="canvas">

  <section class="card card-front" aria-label="Card front">
    <div class="front-header">
      <svg width="340" height="330" viewBox="0 0 340 330" aria-hidden="true">
        <path d="M0 0 H340 V250 Q170 345 0 250 Z" fill="var(--red)"/>
        <path d="M0 0 H340 V238 Q170 330 0 238 Z" fill="var(--navy)"/>
      </svg>
      <div class="front-brand"><span class="brand-dot"></span>Stand Fast</div>
    </div>
    <div class="front-body">
      <h1 class="front-wordmark">Stand Fast</h1>
      <p class="person-name">Dana Whitlock</p>
      <p class="person-title">owner/instructor</p>
      <ul class="contact-list">
        <li class="contact-item">
          <svg width="14" height="14" viewBox="0 0 24 24"><path fill="var(--red)" d="M6.6 10.8a15 15 0 0 0 6.6 6.6l2.2-2.2c.3-.3.7-.4 1-.2 1.1.4 2.3.6 3.6.6.6 0 1 .4 1 1V20c0 .6-.4 1-1 1C10.6 21 3 13.4 3 4c0-.6.4-1 1-1h3.5c.6 0 1 .4 1 1 0 1.3.2 2.5.6 3.6.1.3 0 .7-.2 1z"/></svg>
          208.555.0193
        </li>
        <li class="contact-item">
          <svg width="14" height="14" viewBox="0 0 24 24"><rect x="2" y="5" width="20" height="14" rx="1" fill="var(--red)"/><path d="M2 6l10 7 10-7" stroke="var(--white)" stroke-width="2" fill="none"/></svg>
          dw@sfx-drills.example
        </li>
        <li class="contact-item">
          <svg width="14" height="14" viewBox="0 0 24 24"><circle cx="12" cy="12" r="10" fill="var(--red)"/><path d="M2 12h20M12 2c3 3 3 17 0 20M12 2c-3 3-3 17 0 20" stroke="var(--white)" stroke-width="1.5" fill="none"/></svg>
          www.sfx-drills.example
        </li>
      </ul>
    </div>
  </section>

  <section class="card card-back" aria-label="Card back">
    <div class="back-ring"></div>
    <p class="back-wordmark">Stand <span class="lit">Fast</span></p>
    <p class="back-url">www.SFX-Drills.example</p>
    <div class="badge-row">
      <svg class="badge" viewBox="0 0 74 80" role="img" aria-label="Certification badge"><path d="M37 4 L68 14 V44 Q68 66 37 76 Q6 66 6 44 V14 Z" fill="var(--badge-orange)"/></svg>
      <svg class="badge" viewBox="0 0 74 80" role="img" aria-label="Certification badge"><path d="M37 4 L68 14 V44 Q68 66 37 76 Q6 66 6 44 V14 Z" fill="var(--badge-dark)"/></svg>
      <svg class="badge" viewBox="0 0 74 80" role="img" aria-label="Certification badge"><path d="M37 4 L68 14 V44 Q68 66 37 76 Q6 66 6 44 V14 Z" fill="var(--badge-dark)"/></svg>
      <svg class="badge" viewBox="0 0 74 80" role="img" aria-label="Certification badge"><rect x="6" y="10" width="62" height="60" fill="var(--badge-light)"/></svg>
    </div>
  </section>

</main>
</body>
</html>
```